Small Ecommerce Styled Site to Sell / Lease Domain Names

We have a small portfolio of 100+ domain names that we would like to offer for sale or lease via a web site. Along the lines of http://www.velmorhosts.example/searchdomain.html?priceChoice=2&sort=leasing_desc

We would like initially a 4 page design, listing page (as site referenced above), domain info page (Universal Domain Name Landing Page with form) and checkout a page and About Us Page

We do not want a replica of the site listed, please use it as a guide only, we are looking for a fresh design, in similar concept web 2.0

Our Colours are #351a41 (Main) - #ffca27 (Secondary) all other colours must compliment those 2.
Updates

Domain Landing Page:  I am sorry I was not clear about expectations, however we would like a domain landing page that would be the default holding page for a domain name.

For some examples of what I mean please see:
https://www.qarsibex.example.au/guest-articles/7626-domain-for-sale-landing-pages.html
http://dev.plinthwardexchange.example/blog/2013/09/sales-only-landers-and-buy-it-now-2/

Industry/Entity Type

Domain

Font styles to use
Sans Serif

```html
<!DOCTYPE html>
<html lang="en">
<head>
<meta charset="utf-8">
<title>Leasewell Domains</title>
<link rel="stylesheet" href="https://fonts.googleapis.com/css2?family=Open+Sans:wght@400;600;700&family=Ubuntu:wght@300;400;500;700&display=swap">
<style>
:root{
  --purple:#351a41;
  --purple-deep:#2a1234;
  --yellow:#ffca27;
  --red:#c8202f;
  --ink:#3a3a3a;
  --muted:#8a8a8a;
  --line:#e3e3e3;
  --panel:#f3f4f4;
  --page:#f1f1f1;
  --white:#ffffff;
}
*{box-sizing:border-box;margin:0;padding:0}
html,body{width:790px;height:1200px;overflow:hidden}
body{font-family:"Open Sans",Arial,sans-serif;color:var(--ink);background:var(--white);position:relative}
.abs{position:absolute}
a{color:inherit;text-decoration:none}

/* top bar */
.topbar{left:0;top:0;width:790px;height:25px;background:var(--purple);color:#fff;font-size:7.5px}
.topbar .welcome{position:absolute;left:86px;top:8px;font-weight:600}
.topbar .links{position:absolute;right:90px;top:8px;display:flex;gap:18px}
.topbar .links span{display:flex;align-items:center;gap:4px}
.topbar svg{width:8px;height:8px}

/* header */
.header{left:0;top:25px;width:790px;height:50px;background:var(--white);box-shadow:0 2px 6px rgba(0,0,0,.06);z-index:2}
.logo{position:absolute;left:83px;top:12px;font-family:"Ubuntu",sans-serif;font-weight:700;font-size:24px;color:var(--purple);letter-spacing:-.2px}
.nav{position:absolute;right:88px;top:19px;display:flex;gap:13px;font-family:"Ubuntu",sans-serif;font-size:12px;color:var(--purple)}
.nav .active{color:#f0a500;position:relative}
.nav .active::after{content:"";position:absolute;left:-8px;right:-8px;top:31px;height:2px;background:var(--yellow)}

/* hero */
.hero{left:0;top:75px;width:790px;height:206px;background:linear-gradient(#f6f6f6,#ececec)}
.skyline{left:0;bottom:0;width:790px;height:60px}
.hero h1{position:absolute;left:117px;top:68px;font-family:"Ubuntu",sans-serif;font-weight:500;font-size:20px;color:var(--purple)}
.hero .sub{position:absolute;left:117px;top:91px;font-family:"Ubuntu",sans-serif;font-weight:500;font-size:11px;color:var(--purple)}
.hero .cta{position:absolute;left:118px;top:115px;width:190px;height:30px;background:var(--purple);color:#fff;border-radius:2px;font-family:"Ubuntu",sans-serif;font-weight:500;font-size:13px;padding:7px 0 0 12px}
.hero .cta::after{content:"";position:absolute;right:26px;top:6px;width:1px;height:18px;background:rgba(255,255,255,.3)}
.hero .cta b{position:absolute;right:9px;top:6px;color:var(--yellow);font-size:12px}
.hero-photo{left:515px;top:15px;width:175px;height:191px;background:linear-gradient(180deg,#ececec 0%,#d9dfe4 45%,#bccbd8 100%)}

/* premium band */
.band{left:0;top:281px;width:790px;height:106px;background:var(--yellow)}
.buy-sign{left:86px;top:9px;width:95px;height:97px;background:linear-gradient(160deg,#e0563a,#c8202f)}
.band h2{position:absolute;left:199px;top:27px;font-family:"Ubuntu",sans-serif;font-weight:300;font-size:23px;color:var(--purple)}
.band p{position:absolute;left:199px;top:56px;width:430px;font-size:8.2px;line-height:11.5px;color:#8a6a1e}

/* main */
.main{left:0;top:387px;width:790px;height:583px;background:var(--page)}
.sidebar{left:82px;top:6px;width:213px}
.cat-head{height:29px;background:#fff;border:1px solid var(--line);position:relative;font-family:"Ubuntu",sans-serif;font-size:16px;color:var(--purple);padding:4px 0 0 6px}
.cat-head .tog{position:absolute;right:0;top:5px;width:26px;height:18px;border-left:1px solid var(--line)}
.cat-list{list-style:none}
.cat-list li{height:29px;margin-top:2.4px;background:#fff;border:1px solid var(--line);display:flex;align-items:center;font-size:9.5px;color:#7b7b7b;padding-left:6px;gap:10px}
.plus{width:13px;height:13px;background:#dcdcdc;position:relative;flex:none}
.plus::before,.plus::after{content:"";position:absolute;background:#fff}
.plus::before{left:3px;top:6px;width:7px;height:1.4px}
.plus::after{left:6px;top:3px;width:1.4px;height:7px}
.plus.on{background:var(--yellow)}
.filters{margin-top:2px}
.filter{height:29px;margin-bottom:2.5px;background:var(--purple);color:#fff;font-family:"Ubuntu",sans-serif;font-size:12px;padding:6px 0 0 7px;position:relative}
.filter .tog,.cat-head .tog{display:flex;align-items:center;justify-content:center}
.filter .tog{position:absolute;right:0;top:5px;width:26px;height:19px;border-left:1px solid rgba(255,255,255,.5)}
.tog svg{width:10px;height:6px}

.listing{left:306px;top:6px;width:401px}
.row{height:38px;margin-bottom:4.6px;background:#fff;box-shadow:0 1px 2px rgba(0,0,0,.08);position:relative;display:flex;align-items:center;font-size:8px}
.offer{position:absolute;left:7px;top:5px;width:92px;height:28px;background:var(--yellow);font-size:7.6px;font-weight:700;color:var(--purple);display:flex;align-items:center;justify-content:center}
.row .name{position:absolute;left:111px;font-size:9.5px;color:#666;letter-spacing:.2px}
.row .cat{position:absolute;left:212px;top:8px;height:22px;width:147px;border-left:1px solid var(--line);border-right:1px solid var(--line);display:flex;align-items:center;justify-content:center;font-size:7.3px;color:#6a6a6a}
.row .price{position:absolute;right:10px;font-size:9.5px;color:#555}
.see-more{font-size:9px;color:var(--purple);text-decoration:underline}

.popular{left:306px;top:360px;width:306px;height:223px;background:var(--panel)}
.popular h3{position:absolute;left:23px;top:22px;font-family:"Ubuntu",sans-serif;font-weight:400;font-size:17px;color:var(--purple)}
.pop-table{position:absolute;left:16px;top:59px;width:250px;border-collapse:collapse;font-size:9.5px}
.pop-table td{height:25px;border-bottom:1px solid #dcdcdc;color:#8a8a8a}
.pop-table td:first-child{padding-left:7px;width:138px}
.pop-table td.p{color:#333;width:40px}
.pop-table td.m{border-left:1px solid #dcdcdc;padding-left:8px}
.popular .see-more{position:absolute;left:229px;top:207px;font-size:8px}
.woman{left:612px;top:368px;width:98px;height:215px;background:linear-gradient(180deg,var(--page) 0%,#cfccc9 40%,#a3a09d 100%)}

/* footer */
.footer{left:0;top:970px;width:790px;height:180px;background:var(--purple-deep);color:#fff}
.fcol{position:absolute;top:31px}
.fcol h4{font-family:"Ubuntu",sans-serif;font-weight:400;font-size:12px;width:115px;padding-bottom:3px;border-bottom:1px solid rgba(255,255,255,.8)}
.fcol ul{list-style:none;margin-top:7px;font-size:8.6px;line-height:11.2px}
.contact li{display:flex;gap:7px;margin-bottom:9px;line-height:11.4px}
.contact svg{width:10px;height:13px;flex:none}

.bottom{left:0;top:1150px;width:790px;height:50px;background:#efefef}
.bottom .copy{position:absolute;left:88px;top:20px;font-size:6.8px;color:#8a8a8a}
.social{position:absolute;left:380px;top:21px;display:flex;gap:8px}
.social span{width:7px;height:7px;border-radius:50%;background:#555}
.pay{position:absolute;left:563px;top:16px;display:flex;gap:5px}
.pay span{width:26px;height:16px;border:1px solid #cfcfcf;background:#fff;font-size:5.5px;font-weight:700;color:var(--purple);display:flex;align-items:center;justify-content:center}
</style>
</head>
<body>

<div class="abs topbar">
  <div class="welcome">Default welcome msg!</div>
  <div class="links">
    <span><svg viewBox="0 0 10 10"><rect x="1" y="2" width="7" height="7" fill="none" stroke="#fff"/><path d="M4 6l5-5" stroke="#fff"/></svg>My Account</span>
    <span><svg viewBox="0 0 10 10"><path d="M0 1h2l1.5 5h5l1-4H3" fill="none" stroke="#fff"/><circle cx="4" cy="8.5" r="1" fill="#fff"/><circle cx="8" cy="8.5" r="1" fill="#fff"/></svg>My Cart</span>
    <span><svg viewBox="0 0 10 10"><rect x="0.5" y="1.5" width="9" height="7" fill="none" stroke="#fff"/><path d="M2 4h6M2 6h4" stroke="#fff"/></svg>Checkout</span>
    <span><svg viewBox="0 0 10 10"><circle cx="5" cy="3" r="2.3" fill="#fff"/><path d="M1 10a4 4 0 018 0z" fill="#fff"/></svg>Log In</span>
  </div>
</div>

<header class="abs header">
  <div class="logo">Leasewell Domains</div>
  <nav class="nav"><a class="active">Home</a><a>About</a><a>Pages</a><a>Blog</a><a>Support</a></nav>
</header>

<section class="abs hero">
  <svg class="abs skyline" viewBox="0 0 790 60" preserveAspectRatio="none">
    <g fill="#e0e0e0">
      <rect x="12" y="20" width="70" height="40"/><rect x="75" y="8" width="55" height="52"/><rect x="130" y="30" width="20" height="30"/>
      <rect x="335" y="18" width="45" height="42"/><rect x="380" y="5" width="55" height="55"/><rect x="435" y="25" width="35" height="35"/>
      <rect x="640" y="15" width="40" height="45"/><rect x="715" y="20" width="75" height="40"/>
    </g>
  </svg>
  <h1>Do Come And Lease The Best Domain</h1>
  <div class="sub">Name You Are Interested In FromHome &amp; Garden Category!</div>
  <a class="cta">Find Lease Domains<b>›</b></a>
  <div class="abs hero-photo" role="img" aria-label="Photo of a smiling man in a light blue shirt with arms crossed"></div>
</section>

<section class="abs band">
  <div class="abs buy-sign" role="img" aria-label="Illustration of a red signpost with a hanging BUY sign"></div>
  <h2>Premium Domains</h2>
  <p>Velmor Domains has over six million available domain names ready to become businesses. Read the smart purchases below to inspire your own domain name search.</p>
</section>

<main class="abs main">
  <aside class="abs sidebar">
    <div class="cat-head">Categories<span class="tog"><svg viewBox="0 0 10 6"><path d="M1 5l4-4 4 4" fill="none" stroke="#351a41"/></svg></span></div>
    <ul class="cat-list">
      <li><span class="plus on"></span>Automotive</li>
      <li><span class="plus"></span>Business and Finance</li>
      <li><span class="plus"></span>Computers and Internet</li>
      <li><span class="plus"></span>Education</li>
      <li><span class="plus"></span>Entertainment</li>
      <li><span class="plus"></span>Family</li>
      <li><span class="plus"></span>Food and Beverage</li>
      <li><span class="plus"></span>Games</li>
      <li><span class="plus"></span>Home and Garden</li>
      <li><span class="plus"></span>Health and Beauty</li>
      <li><span class="plus"></span>Lifestyle</li>
      <li><span class="plus"></span>Shopping</li>
    </ul>
    <div class="filters">
      <div class="filter">Extensions<span class="tog"><svg viewBox="0 0 10 6"><path d="M1 1l4 4 4-4" fill="none" stroke="#fff"/></svg></span></div>
      <div class="filter">Price Range<span class="tog"><svg viewBox="0 0 10 6"><path d="M1 1l4 4 4-4" fill="none" stroke="#fff"/></svg></span></div>
      <div class="filter">Word Count<span class="tog"><svg viewBox="0 0 10 6"><path d="M1 1l4 4 4-4" fill="none" stroke="#fff"/></svg></span></div>
      <div class="filter">Word Structure<span class="tog"><svg viewBox="0 0 10 6"><path d="M1 1l4 4 4-4" fill="none" stroke="#fff"/></svg></span></div>
      <div class="filter">Language<span class="tog"><svg viewBox="0 0 10 6"><path d="M1 1l4 4 4-4" fill="none" stroke="#fff"/></svg></span></div>
    </div>
  </aside>

  <section class="abs listing">
    <div class="row"><a class="offer">Make Offer</a><span class="name">TIDEWADERS.COM</span><span class="cat">Categories / Business and Finance</span><span class="price">$2,088</span></div>
    <div class="row"><a class="offer">Make Offer</a><span class="name">BREEZEVAULT.COM</span><span class="cat">Categories / Computers and Internet</span><span class="price">$2,088</span></div>
    <div class="row"><a class="offer">Make Offer</a><span class="name">DUNEHARBOR.COM</span><span class="cat">Categories / Business and Finance</span><span class="price">$2,088</span></div>
    <div class="row"><a class="offer">Make Offer</a><span class="name">MOTORGAVEL.COM</span><span class="cat">Categories / Business and Finance</span><span class="price">$2,088</span></div>
    <div class="row"><a class="offer">Make Offer</a><span class="name">TIDEWADERS.COM</span><span class="cat">Categories / Business and Finance</span><span class="price">$2,088</span></div>
    <div class="row"><a class="offer">Make Offer</a><span class="name">BREEZEVAULT.COM</span><span class="cat">Categories / Business and Finance</span><span class="price">$2,088</span></div>
    <div class="row"><a class="offer">Make Offer</a><span class="name">DUNEHARBOR.COM</span><span class="cat">Categories / Business and Finance</span><span class="price">$2,088</span></div>
    <div class="row"><a class="offer">Make Offer</a><span class="name">MOTORGAVEL.COM</span><span class="cat">Categories / Business and Finance</span><span class="price">$2,088</span></div>
    <div style="text-align:right;margin-top:-2px"><a class="see-more">See more</a></div>
  </section>

  <section class="abs popular">
    <h3>Popular Domains</h3>
    <table class="pop-table">
      <tr><td>Quillet.com</td><td class="p">$1050</td><td class="m">Make Offer</td></tr>
      <tr><td>TuneSnip.com</td><td class="p">$100</td><td class="m">Make Offer</td></tr>
      <tr><td>TuneSnip.com</td><td class="p">$700</td><td class="m">Make Offer</td></tr>
      <tr><td>MixLoft.com</td><td class="p">$400</td><td class="m">Make Offer</td></tr>
      <tr><td>Trakko.com</td><td class="p">$900</td><td class="m">Make Offer</td></tr>
      <tr><td>Quillet.com</td><td class="p">$1050</td><td class="m">Make Offer</td></tr>
    </table>
    <a class="see-more">See more</a>
  </section>
  <div class="abs woman" role="img" aria-label="Photo of a smiling businesswoman in a grey blazer"></div>
</main>

<footer class="abs footer">
  <div class="fcol" style="left:89px"><h4>Categories</h4>
    <ul><li>Automotive</li><li>Business and Finance</li><li>Computers and Internet</li><li>Education</li><li>Entertainment</li><li>Family</li><li>Food and Beverage</li></ul></div>
  <div class="fcol" style="left:245px"><h4>About Us</h4>
    <ul><li>Join our newsletter!</li><li>About Us</li><li>News</li><li>Blog</li><li>Success Stories</li><li>Membership Contract</li><li>Privacy Policy</li></ul></div>
  <div class="fcol" style="left:407px"><h4>Buy Domains</h4>
    <ul><li>Premium Domains</li><li>Bargain Domains</li><li>Popular Domains</li><li>Top keywords</li></ul></div>
  <div class="fcol contact" style="left:548px"><h4>Contact Us</h4>
    <ul>
      <li><svg viewBox="0 0 10 13"><path d="M5 0a4.5 4.5 0 00-4.5 4.5C.5 8 5 13 5 13s4.5-5 4.5-8.5A4.5 4.5 0 005 0z" fill="#ffca27"/><circle cx="5" cy="4.5" r="1.7" fill="#2a1234"/></svg><span>Brightfield Holdings Corp.&nbsp; Route 42<br>P.O. Box 310&nbsp; Larkport, ME 04999</span></li>
      <li><svg viewBox="0 0 10 13"><rect x="1" y="0.5" width="8" height="12" rx="1" fill="#ffca27"/><path d="M3 3l4 7M7 3l-4 7" stroke="#2a1234"/></svg><span>555.014.2290</span></li>
      <li><svg viewBox="0 0 10 13"><rect x="1.5" y="0.5" width="7" height="12" rx="1.2" fill="none" stroke="#ffca27"/><circle cx="5" cy="10.5" r=".8" fill="#ffca27"/></svg><span>info@brightfieldholdings.example</span></li>
    </ul></div>
</footer>

<div class="abs bottom">
  <div class="copy">CopyRight @Leasewell Domains all right reserved</div>
  <div class="social"><span></span><span></span><span></span><span></span><span></span></div>
  <div class="pay"><span>Payvo</span><span>Cardix</span><span>Norra</span><span>Meridia</span><span>Tallo</span></div>
</div>

</body>
</html>
```